snugTAB - packaging design for plastic zip-lock mechansim

Looking for packaging designs for my patented product, which provides the ability to lock and close existing plastic bags, which have been opened up (like sugar or flour bag, snack bag, etc.). With applying snugTAB to any bag once opened, the products can be held safe, locked and dry.
Please check my supporting documentation attached, including logos and packaging description.
The packaging design has to make clear to the customer:
- WHAT is this product for
- how to USA
- what are the BENEFITS and the VALUE
I am looking for a long term cooperation with the winning designer, as I will need multiple variations of the packaging depending on individual product usage. I am thinking of approximately 10 different variations in the future.
Updates
Project Deadline Extended Reason: Extending deadline to receive more designs. Please submit your designs according to my description. Let me know if any questions!This will be a long term cooperation as I will need subsequent designs for alternative product variations in the future. Added Saturday, October 22, 2016
Target Market(s)
All consumers who buy products in the supermarket. In particular when they buy products in bags (like salt, sugar, flour, detergents, snacks, ...)
Industry/Entity Type
Retail
Look and feel
Each slider illustrates characteristics of the customer's brand and the style your logo design should communicate.

```html
<!DOCTYPE html>
<html lang="en">
<head>
<meta charset="utf-8">
<title>snugTAB packaging – layout sheet</title>
<link href="https://fonts.googleapis.com/css2?family=Signika:wght@400;600&family=Arimo:wght@400&display=swap" rel="stylesheet">
<style>
  :root{
    --yellow:#ffcc00;
    --ink:#1d1d1b;
    --white:#ffffff;
    --guide:#9a9a9a;
    --sleeve:#eef0ef;
    --wood-dark:#3a2418;
    --wood-mid:#7a4a2a;
    --wood-light:#b98a5c;
    --cyan:#1a9ee0;
    --magenta:#e5157d;
    --key:#222222;
  }
  *{box-sizing:border-box;margin:0;padding:0}
  html,body{width:841px;height:1200px;overflow:hidden;background:var(--white)}
  body{position:relative;font-family:"Arimo",Arial,sans-serif;color:var(--ink);border:1px solid #777}
  .abs{position:absolute}
  .hline{position:absolute;height:1px;background:var(--guide)}
  .vline{position:absolute;width:1px;background:var(--guide)}
  .label{position:absolute;font-size:16px;line-height:19px}

  /* package face (front + clip) */
  .face{position:absolute;width:261px;height:400px;overflow:hidden}
  .face .photo{position:absolute;left:0;top:0;width:261px;height:360px;
    background:linear-gradient(180deg,var(--wood-dark) 0%,var(--wood-mid) 35%,#6f7a70 48%,var(--wood-light) 66%,#d9cfbd 82%,#efe8da 100%)}
  .face .band{position:absolute;left:0;top:360px;width:261px;height:40px;background:var(--yellow)}
  .face .brand{position:absolute;left:0;top:360px;width:261px;height:40px;text-align:center;
    font-family:"Signika",sans-serif;font-weight:600;font-size:29px;line-height:40px;color:var(--ink)}
  .face .headline{position:absolute;left:41px;top:66px;font-family:"Signika",sans-serif;font-weight:600;
    font-size:27px;line-height:32px;color:var(--white);text-shadow:1px 1px 3px #000}
  .face .tagline{position:absolute;left:11px;top:208px;font-family:"Signika",sans-serif;
    font-size:23px;color:var(--white);text-shadow:1px 1px 3px #000}
  .face .count{position:absolute;left:190px;top:290px;font-family:"Signika",sans-serif;font-weight:600;
    font-size:62px;line-height:62px;color:var(--white);text-shadow:2px 2px 4px #000}
  .face .count small{font-size:16px;font-weight:400}
  .hanger{position:absolute}

  /* back side */
  .back{position:absolute;left:485px;top:67px;width:259px;height:399px;background:var(--yellow)}
  .back .divider{position:absolute;left:0;width:259px;height:2px;background:var(--white)}
  .back .flip{position:absolute;transform:rotate(180deg);font-size:11px;line-height:16px;color:var(--ink)}
  .back .swatch{position:absolute;background:var(--white)}
  .back .howto{position:absolute;left:0;top:330px;width:259px;text-align:center;transform:rotate(180deg);font-size:16px}

  .strip{position:absolute;left:364px;top:67px;width:20px;height:399px;background:var(--yellow)}
  .strip .edge{position:absolute;left:0;top:0;width:8px;height:360px;background:linear-gradient(180deg,var(--wood-dark),var(--wood-light))}

  .sleeve{position:absolute;left:94px;top:466px;width:242px;height:642px;background:var(--sleeve)}
  .sleeve-edge{position:absolute;left:364px;top:466px;width:20px;height:642px;background:var(--sleeve);border-left:1px solid #d6d8d7}

  .legend{position:absolute;left:484px;font-size:12px}
  .legend i{display:inline-block;width:15px;height:15px;border-radius:50%;vertical-align:middle;margin-right:8px}
  .rot{position:absolute;transform:rotate(-90deg);transform-origin:center;font-size:14px;white-space:nowrap}
</style>
</head>
<body>

<!-- guides -->
<div class="hline" style="left:64px;top:66px;width:706px"></div>
<div class="vline" style="left:85px;top:48px;height:1128px"></div>
<div class="vline" style="left:346px;top:48px;height:1128px"></div>
<div class="hline" style="left:744px;top:466px;width:32px"></div>
<div class="hline" style="left:446px;top:864px;width:330px"></div>
<div class="hline" style="left:69px;top:1108px;width:387px"></div>

<!-- clip face -->
<div class="face" style="left:85px;top:66px">
  <div class="photo" role="img" aria-label="Photo of a wooden kitchen counter with pot, plates and cups"></div>
  <svg class="hanger" style="left:101px;top:10px" width="58" height="23" viewBox="0 0 58 23"><path d="M4 10h17a8 8 0 0 1 16 0h17a4 4 0 0 1 4 4v5a4 4 0 0 1-4 4H4a4 4 0 0 1-4-4v-5a4 4 0 0 1 4-4z" fill="#fff"/></svg>
  <div class="headline">THE PERFECT<br>SOLUTION<br>FOR CLOSING<br>PLASTIC BAGS</div>
  <div class="tagline">kitchen or everywhere</div>
  <div class="count">5<small>pcs</small></div>
  <div class="band"></div>
  <div class="brand">snugTAB</div>
</div>
<div class="label" style="left:46px;top:274px">clip</div>

<div class="sleeve"></div>
<div class="label" style="left:94px;top:835px;width:242px;text-align:center">plastic sleeve</div>

<div class="strip"><div class="edge"></div></div>
<div class="sleeve-edge"></div>

<!-- dimensions -->
<svg class="abs" style="left:0;top:0" width="841" height="1200">
  <g stroke="#222" stroke-width="1" fill="#222">
    <line x1="414" y1="68" x2="414" y2="1107"/>
    <path d="M410 76 414 67 418 76z"/><path d="M410 1099 414 1108 418 1099z"/>
    <line x1="455" y1="68" x2="455" y2="465"/>
    <path d="M451 76 455 67 459 76z"/><path d="M451 457 455 466 459 457z"/>
    <line x1="455" y1="467" x2="455" y2="863"/>
    <path d="M451 475 455 466 459 475z"/><path d="M451 855 455 864 459 855z"/>
    <line x1="86" y1="1152" x2="345" y2="1152"/>
    <path d="M94 1148 85 1152 94 1156z"/><path d="M337 1148 346 1152 337 1156z"/>
  </g>
</svg>
<div class="rot" style="left:370px;top:587px">260 mms</div>
<div class="rot" style="left:415px;top:282px">100 mms</div>
<div class="rot" style="left:415px;top:681px">100 mms</div>
<div class="label" style="left:174px;top:1132px;font-size:14px">65 mms</div>

<!-- back side -->
<div class="back">
  <div class="swatch" style="left:19px;top:10px;width:97px;height:49px"></div>
  <div class="flip" style="left:19px;top:10px;width:97px;height:49px;line-height:49px;text-align:center;font-size:15px">code</div>
  <div class="flip" style="left:137px;top:10px">lorem ipsum lorem<br>lorem ipsum lorem<br>lorem ipsum lorem</div>
  <div class="divider" style="top:72px"></div>
  <div class="flip" style="left:34px;top:81px">lorem ipsum ipsum<br>lorem ipsum ipsum<br>lorem ipsum ipsum<br>lorem ipsum ipsum</div>
  <div class="swatch" style="left:183px;top:85px;width:59px;height:59px"></div>
  <div class="divider" style="top:154px"></div>
  <div class="flip" style="left:34px;top:163px">lorem ipsum ipsum<br>lorem ipsum ipsum<br>lorem ipsum ipsum<br>lorem ipsum ipsum</div>
  <div class="swatch" style="left:183px;top:165px;width:59px;height:59px"></div>
  <div class="divider" style="top:234px"></div>
  <div class="flip" style="left:34px;top:242px">lorem ipsum ipsum<br>lorem ipsum ipsum<br>lorem ipsum ipsum<br>lorem ipsum ipsum</div>
  <div class="swatch" style="left:183px;top:245px;width:59px;height:59px"></div>
  <div class="divider" style="top:316px"></div>
  <div class="howto">How to use</div>
  <svg class="hanger" style="left:100px;top:362px" width="62" height="25" viewBox="0 0 62 25"><path d="M4 0h54a4 4 0 0 1 4 4v5a4 4 0 0 1-4 4H39a8 8 0 0 1-16 0H4a4 4 0 0 1-4-4V4a4 4 0 0 1 4-4z" fill="#fff"/></svg>
</div>
<div class="label" style="left:775px;top:268px">back<br>side</div>

<!-- front face -->
<div class="face" style="left:485px;top:466px;width:259px">
  <div class="photo" role="img" aria-label="Photo of a wooden kitchen counter with pot, plates and cups"></div>
  <svg class="hanger" style="left:100px;top:8px" width="58" height="23" viewBox="0 0 58 23"><path d="M4 10h17a8 8 0 0 1 16 0h17a4 4 0 0 1 4 4v5a4 4 0 0 1-4 4H4a4 4 0 0 1-4-4v-5a4 4 0 0 1 4-4z" fill="#fff"/></svg>
  <div class="headline" style="top:64px">THE PERFECT<br>SOLUTION<br>FOR CLOSING<br>PLASTIC BAGS</div>
  <div class="tagline" style="top:204px">kitchen or everywhere</div>
  <div class="count" style="top:286px">5<small>pcs</small></div>
  <div class="band"></div>
  <div class="brand">snugTAB</div>
</div>
<div class="label" style="left:775px;top:668px">front<br>side</div>

<!-- project notes -->
<div class="label" style="left:485px;top:898px">Project: snugTAB packaging</div>
<div class="legend" style="top:938px"><i style="background:var(--cyan)"></i>cyan</div>
<div class="legend" style="top:958px"><i style="background:var(--magenta)"></i>magenta</div>
<div class="legend" style="top:978px"><i style="background:var(--yellow)"></i>yellow</div>
<div class="legend" style="top:998px"><i style="background:var(--key)"></i>black</div>
<div class="label" style="left:486px;top:1054px">Material:- cardboard 250g</div>
<div class="label" style="left:551px;top:1074px">- plastic sleeve, 60 mms wide</div>
<div class="label" style="left:561px;top:1093px">welded and &nbsp;perforated</div>
<div class="label" style="left:561px;top:1112px">á 260 mms</div>
<div class="label" style="left:486px;top:1148px">M=1:1</div>

</body>
</html>
```